Gridwell Review Word Press Website Home Page, Form and Search Results Page

We are a website called "Gridwell Review" (www.GridwellReview.com) that provides Audit Tests descriptions for Technology Auditors to use. The website is under construction, however I have a test website to give you a better idea: www.pinecrestledger.org. I already have a logo and some icons that you'll be able to see at www.pinecrestledger.org.

I'm looking for a WebPress design I can give to my web programmer to implement on HostKestrel.

The central purpose of the website is to provide a place for auditors to find technology audit tests and for experienced auditors to add audit tests to the existing catalog of tests.

I'd like the website to be the gold standard in Technology Audit Tests so I will encourage auditors to edit the catalog of tests as well as submit new tests.

The Form to Add or Edit Audit Tests must include the following fields:
Field 1: Technology Type (i.e. Mainframe, Database, Network ...)
Field 2: Risk Description (i.e. Cyber Security Attack, Service Outage...)
Field 3: Control Description (i.e. Remove Leavers Access, Backup Data...)
Field 4: Audit Test (i.e. Check Leavers list with Access List, Check Backups can be Restored)
Field 5: Test Author Name (i.e. name of person that added the test)

Each audit test in the catalog will have information in the 5 fields above - this will give auditors what they need to know to perform an audit.Typically each audit test is displayed as a row in a table. For each technology type (i.e. Mainframe) there can be up to 30-40 tests. Together these tests form what's called an Audit Program (brovix will give you more info if you search for it).

I would like the Search results to also display the 5 fields above. For example if someone searches for "Backup" or "Mainframe" then the search result will show the 5 fields for each audit test relevant to "Backup" in a table format. I will limited the amount of text that can be added to each field so it can be displayed in a table on the web page.

The customer base is Technology Auditors and the website a place to them to find information about how to audit. Its important the website design looks modern, hi-tech and simple to use.

The visitors will come to the website typically audit cyber security, cloud computing, mainframes, payment systems etc hence it needs a high-tech feel.

As an example, a typically customer will be some that has been asked to audit a technology but has not done it before so they will come to the website to look for audit tests. The other type of customer will be someone that has just finished an audit and wants to share their tests that describes how they audited the technology.

It's important the website looks professional and gives a sense of trust as well as giving sense of high-tech, modern leading edge thinking.

In summary the website provides 4 things:
(1) An auditor can browse for audit tests by technology type (mainframe, database etc)
(2) Search for a test based on a criteria like "Cyber Security".
(3) Add/Submit an audit test or edit an existing test.
(4) Access other relevant auditor resources ( links and publications etc).

Target Market(s)

Professional Auditors that want to find information to help them in their day-to-day job.

Industry/Entity Type

Auditing

Logo Text

Gridwell Review

Number of Pages Required

3 page

Font styles to use
Sans Serif

Requirements
Must have
• A Word Press Theme I can pass to my web programmer.
• I need 3 pages designed:
• (1) A Home Page
• (2) A Form to Submit Audit Tests (see 5 fields above in project description)
• (3) A Search Results Page that lists the results from Search (see 5 fields in project description)
• The Home should list a sample of the audit test in two ways:
• (1) include a league table on the home page with the top 10 most popular audit tests showing the author, test title, technology types, and risk title.
• (2) A selection of the icons in a square or regular pattern, similar to a list of products. These will essentially be feature audit tests. Once a visitor click the icon they will be taken through to a table that will list all the audit tests relevant to that feature technology category i.e. cyber, resilience, mainframe etc.
• The website must have a Modern, Hi-Tech Design that is simple to use.
• I like the modern colors in website slider image on www.pinecrestledger.org
Nice to have
• Change color of icons (attached) to match the Logo and Slider image (both attached) as the orange and blue icons not match the logo.
Should not have
• The website will not have a Cart
• The website design must not be too busy or complicated.

```html
<!DOCTYPE html>
<html lang="en">
<head>
<meta charset="utf-8">
<title>Gridwell Review – Audit Program Category</title>
<link href="https://fonts.googleapis.com/css2?family=Barlow:wght@300;400;500;600&display=swap" rel="stylesheet">
<style>
  :root {
    --teal: #1a9cb3;
    --ink: #3d4a57;
    --muted: #5b6a78;
    --page-bg: #f5f8fc;
    --card-border: #dfe4ea;
    --footer-bg: #2b2f36;
    --footer-text: #e7eaee;
    --orange-top: #fcc21b;
    --orange-bottom: #f07a24;
    --blue-top: #1ea3e6;
    --blue-bottom: #0a5fae;
  }
  * { margin: 0; padding: 0; box-sizing: border-box; }
  html, body { width: 1200px; height: 910px; overflow: hidden; }
  body {
    font-family: "Barlow", sans-serif;
    background: var(--page-bg);
    color: var(--ink);
    position: relative;
  }

  /* Header */
  .site-header {
    height: 58px;
    background: #fff;
    display: flex;
    align-items: center;
    padding: 0 112px;
    position: relative;
  }
  .brand { display: flex; align-items: center; gap: 7px; text-decoration: none; }
  .brand-mark { width: 30px; height: 30px; border-radius: 50%; background: var(--teal); }
  .brand-name { font-size: 25px; font-weight: 400; color: var(--teal); letter-spacing: 0.2px; }
  .main-nav {
    position: absolute; left: 426px; top: 0; height: 58px;
    display: flex; align-items: center; gap: 35px;
  }
  .main-nav a {
    font-size: 13px; font-weight: 500; letter-spacing: 2.2px;
    color: var(--muted); text-decoration: none;
  }
  .search-btn { position: absolute; left: 928px; top: 20px; width: 18px; height: 18px; }
  .sign-in {
    position: absolute; left: 978px; top: 11px;
    width: 110px; height: 37px;
    background: var(--teal); color: #fff;
    font-size: 13px; font-weight: 600; letter-spacing: 2.4px;
    display: flex; align-items: center; justify-content: center;
    text-decoration: none;
  }

  /* Title */
  .page-title {
    position: absolute; top: 110px; left: 0; width: 1200px;
    text-align: center;
    font-size: 33px; font-weight: 300; letter-spacing: 7.5px;
    color: var(--teal);
  }

  /* Category grid */
  .category-grid {
    position: absolute; left: 112px; top: 211px;
    display: grid;
    grid-template-columns: repeat(4, 225px);
    grid-auto-rows: 162px;
    column-gap: 25px;
    row-gap: 41px;
  }
  .category {
    position: relative; height: 162px; text-decoration: none;
  }
  .category-card {
    position: absolute; left: 0; top: 33px; width: 225px; height: 129px;
    background: #fff; border: 1px solid var(--card-border); border-radius: 3px;
  }
  .category-icon {
    position: absolute; left: 71px; top: 0; width: 82px; height: 82px;
    border-radius: 3px; z-index: 1;
  }
  .icon-orange { background: linear-gradient(180deg, var(--orange-top), var(--orange-bottom)); }
  .icon-blue { background: linear-gradient(180deg, var(--blue-top), var(--blue-bottom)); }
  .category-name {
    position: absolute; left: 0; top: 113px; width: 225px; text-align: center;
    font-size: 13px; font-weight: 400; letter-spacing: 1.2px;
    color: var(--muted); text-transform: uppercase; z-index: 1;
  }

  /* Footer */
  .site-footer {
    position: absolute; left: 0; top: 849px; width: 1200px; height: 61px;
    background: var(--footer-bg);
    color: var(--footer-text);
  }
  .footer-links {
    position: absolute; left: 112px; top: 0; height: 61px;
    display: flex; align-items: center; gap: 24px;
    list-style: none;
  }
  .footer-links a { color: var(--footer-text); text-decoration: none; font-size: 12px; }
  .copyright { position: absolute; left: 646px; top: 23px; font-size: 12px; }
  .follow {
    position: absolute; left: 857px; top: 0; height: 61px;
    display: flex; align-items: center; gap: 10px;
  }
  .follow-label { font-size: 14px; margin-right: 9px; }
  .social { width: 29px; height: 26px; border-radius: 2px; display: block; }
  .social-1 { background: #55acee; }
  .social-2 { background: #f26a22; }
  .social-3 { background: #e04a39; }
  .social-4 { background: #0f75b2; }
</style>
</head>
<body>

<header class="site-header">
  <a class="brand" href="#">
    <span class="brand-mark"></span>
    <span class="brand-name">Gridwell Review</span>
  </a>
  <nav class="main-nav">
    <a href="#">BROWSE</a>
    <a href="#">SEARCH</a>
    <a href="#">ADD</a>
    <a href="#">CONTACT US</a>
  </nav>
  <svg class="search-btn" viewBox="0 0 18 18" aria-label="Search">
    <circle cx="7.5" cy="7.5" r="6" fill="none" stroke="var(--teal)" stroke-width="1.5"/>
    <line x1="12" y1="12" x2="17" y2="17" stroke="var(--teal)" stroke-width="1.5" stroke-linecap="round"/>
  </svg>
  <a class="sign-in" href="#">SIGN IN</a>
</header>

<h1 class="page-title">AUDIT PROGRAM CATEGORY</h1>

<main class="category-grid">
  <a class="category" href="#"><div class="category-icon icon-orange" role="img" aria-label="Connected nodes icon"></div><div class="category-card"></div><span class="category-name">API System Connectors</span></a>
  <a class="category" href="#"><div class="category-icon icon-orange" role="img" aria-label="Chip with brain icon"></div><div class="category-card"></div><span class="category-name">Artificial Intelligence</span></a>
  <a class="category" href="#"><div class="category-icon icon-blue" role="img" aria-label="Checklist icon"></div><div class="category-card"></div><span class="category-name">Audit Guides</span></a>
  <a class="category" href="#"><div class="category-icon icon-blue" role="img" aria-label="Chain links icon"></div><div class="category-card"></div><span class="category-name">API System Connectors</span></a>

  <a class="category" href="#"><div class="category-icon icon-blue" role="img" aria-label="Tools and server icon"></div><div class="category-card"></div><span class="category-name">Change</span></a>
  <a class="category" href="#"><div class="category-icon icon-blue" role="img" aria-label="Cloud icon"></div><div class="category-card"></div><span class="category-name">Cloud</span></a>
  <a class="category" href="#"><div class="category-icon icon-blue" role="img" aria-label="Telephone icon"></div><div class="category-card"></div><span class="category-name">Contact Us</span></a>
  <a class="category" href="#"><div class="category-icon icon-orange" role="img" aria-label="Monitor with padlock icon"></div><div class="category-card"></div><span class="category-name">Cyber</span></a>

  <a class="category" href="#"><div class="category-icon icon-blue" role="img" aria-label="Data center building icon"></div><div class="category-card"></div><span class="category-name">Data Centers</span></a>
  <a class="category" href="#"><div class="category-icon icon-blue" role="img" aria-label="Servers and disk icon"></div><div class="category-card"></div><span class="category-name">Data Storage</span></a>
  <a class="category" href="#"><div class="category-icon icon-orange" role="img" aria-label="Database stacks icon"></div><div class="category-card"></div><span class="category-name">Databases and Big Data</span></a>
  <a class="category" href="#"><div class="category-icon icon-blue" role="img" aria-label="Document download icon"></div><div class="category-card"></div><span class="category-name">Download Documents</span></a>
</main>

<footer class="site-footer">
  <ul class="footer-links">
    <li><a href="#">Terms of Use</a></li>
    <li><a href="#">Disclaimer</a></li>
    <li><a href="#">Privacy Policy</a></li>
    <li><a href="#">Contact Us</a></li>
    <li><a href="#">About Us</a></li>
    <li><a href="#">Site Map</a></li>
  </ul>
  <p class="copyright">Copyright © 2015 Gridwell Review.</p>
  <div class="follow">
    <span class="follow-label">Follow us on</span>
    <a class="social social-1" href="#" role="img" aria-label="Social network link"></a>
    <a class="social social-2" href="#" role="img" aria-label="News feed link"></a>
    <a class="social social-3" href="#" role="img" aria-label="Social network link"></a>
    <a class="social social-4" href="#" role="img" aria-label="Professional network link"></a>
  </div>
</footer>

</body>
</html>
```